Intermodal Trucking Company Website

My client is a trucking company that takes the containers you see on the back of a ship or railroad car and delivers them in the midwestern part of the United States. Here are some of their competitors Websites and their logo to use as part of the design.

http://www.varnekhaulers.example/
https://www.plirext.example/
http://www.brontagefreight.example/
https://www.lqp-xy.example/

Industry/Entity Type

Trucking Company

Number of Pages Required

2 page

Requirements
Must have
• Website must be professional and the design needs to be suitable for a responsive Website.
Should not have
• Please do not submit designs with misspellings. Designs with misspellings will be eliminated.

```html
<!DOCTYPE html>
<html lang="en">
<head>
<meta charset="utf-8">
<title>Northmark Haul Co. – Intermodal Trucking</title>
<link href="https://fonts.googleapis.com/css2?family=Open+Sans:wght@400;600;700;800&display=swap" rel="stylesheet">
<style>
:root{
  --orange:#f26522;
  --orange-dark:#d9531a;
  --ink:#2b2b2b;
  --text:#666;
  --muted:#999;
  --light:#f0f0f0;
  --line:#dddddd;
  --navy:#1b2430;
  --navy-2:#242f3d;
  --white:#fff;
}
*{box-sizing:border-box;margin:0;padding:0}
html,body{width:1200px;height:3584px;overflow:hidden}
body{font-family:"Open Sans",Arial,sans-serif;color:var(--text);background:var(--white);font-size:15px;line-height:1.6}
.wrap{width:1040px;margin:0 auto;position:relative}
.section-title{text-align:center;font-size:40px;font-weight:800;color:var(--ink);text-transform:uppercase;letter-spacing:1px;position:relative;padding-bottom:14px}
.section-title span{color:var(--orange)}
.section-title::after{content:"";position:absolute;left:50%;bottom:0;width:80px;height:4px;margin-left:-40px;background:var(--orange)}
.section-title.left{text-align:left}
.section-title.left::after{left:0;margin-left:0}
.btn{display:inline-block;background:var(--orange);color:var(--white);font-weight:700;font-size:15px;text-transform:uppercase;padding:10px 28px;border-radius:3px}

/* hero */
.hero{height:640px;position:relative;background:linear-gradient(180deg,#c9d9e6 0%,#9fb6c9 45%,#6f879c 100%)}
.hero-photo{position:absolute;inset:0}
.nav{position:absolute;top:0;left:0;right:0;height:70px;background:rgba(255,255,255,.92);display:flex;align-items:center;padding:0 100px;font-size:15px;font-weight:700;text-transform:uppercase;color:var(--ink)}
.nav a{padding:0 20px;line-height:70px}
.nav a.active{background:var(--orange);color:var(--white)}
.nav .spacer{flex:1}
.brand{position:absolute;top:14px;left:50%;transform:translateX(-50%);width:230px;height:150px;border-radius:50%;background:var(--white);display:flex;align-items:center;justify-content:center;gap:10px;box-shadow:0 2px 10px rgba(0,0,0,.2)}
.brand-dot{width:16px;height:16px;border-radius:50%;background:var(--orange)}
.brand-name{font-size:20px;font-weight:800;color:var(--navy);text-align:center;line-height:1.2}
.hero-copy{position:absolute;top:440px;left:0;right:0;text-align:center}
.hero-copy h1{font-size:36px;font-weight:800;color:var(--white);text-transform:uppercase;text-shadow:0 2px 6px rgba(0,0,0,.35);margin-bottom:20px}

/* about */
.about{height:360px;padding-top:60px;text-align:center}
.about p{margin-top:28px;font-size:15px;line-height:1.8}
.about p + p{margin-top:12px}

/* services */
.services{height:560px;background:var(--light);padding-top:40px}
.services .lead{text-align:center;margin:24px auto 28px;width:900px;font-size:14px}
.cards{display:flex;gap:20px}
.card{width:333px;background:var(--white);text-align:center;padding-bottom:20px}
.card .photo{height:170px}
.card h3{font-size:18px;font-weight:800;color:var(--ink);text-transform:uppercase;margin:18px 0 6px}
.card p{font-size:14px;padding:0 30px;margin-bottom:16px}
.card .btn{font-size:13px;padding:6px 22px}
.arrow{position:absolute;top:240px;width:30px;height:60px}
.arrow.l{left:-60px}.arrow.r{right:-60px}

/* why */
.why{height:580px;padding-top:60px;position:relative}
.why-grid{position:relative;height:440px;margin-top:40px}
.person{position:absolute;left:330px;top:0;width:380px;height:440px;background:linear-gradient(180deg,#e9ecef 0%,#bfc6cf 60%,#8e97a3 100%)}
.feature{position:absolute;width:300px}
.feature .icon{width:46px;height:46px;border-radius:50%;background:var(--navy-2);display:flex;align-items:center;justify-content:center;margin-bottom:8px}
.feature.hot .icon{background:var(--orange)}
.feature h4{font-size:16px;font-weight:700;color:var(--ink)}
.feature.hot h4{color:var(--orange)}
.feature p{font-size:13px;line-height:1.5}
.feature.left{text-align:right}
.feature.left .icon{margin-left:auto}

/* team */
.team{height:460px;background:var(--light);padding-top:50px}
.members{display:flex;gap:20px;margin-top:44px}
.member{width:245px;height:260px;position:relative;background:linear-gradient(180deg,#d7d3cf,#9a948e)}
.member .cap{position:absolute;left:0;right:0;bottom:0;background:rgba(242,101,34,.92);color:var(--white);text-align:center;padding:8px 0}
.member .cap b{display:block;font-size:15px}
.member .cap small{font-size:12px}
.member.open{background:var(--orange);color:var(--white);text-align:center;padding:30px 22px}
.member.open b{font-size:16px;display:block;margin-bottom:2px}
.member.open small{font-size:12px;display:block;margin-bottom:12px}
.member.open p{font-size:13px;line-height:1.6;margin-bottom:16px}
.socials{display:flex;justify-content:center;gap:8px}
.socials i{width:26px;height:26px;border-radius:50%;background:var(--white);display:block}

/* news & testimonials */
.split{height:440px;padding-top:40px;display:flex;gap:60px}
.news{width:460px}
.news-item{display:flex;gap:18px;margin-top:36px}
.news-item + .news-item{margin-top:24px}
.news-item .thumb{width:120px;height:80px;flex:none;background:linear-gradient(180deg,#b9c7d3,#6e7f8e)}
.news-item h5{font-size:14px;color:var(--orange);font-weight:700;line-height:1.4}
.news-item p{font-size:12.5px;line-height:1.5}
.news-item time{font-size:11px;color:var(--muted)}
.news .btn{margin-top:26px;font-size:13px;padding:6px 18px}
.testis{flex:1}
.testi-box{margin-top:36px;background:var(--light);padding:22px}
.testi{display:flex;gap:16px}
.testi + .testi{margin-top:22px}
.avatar{width:64px;height:64px;border-radius:50%;flex:none;background:linear-gradient(180deg,#c8c2bc,#857d76)}
.testi b{font-size:14px;color:var(--ink)}
.testi p{font-size:12.5px;line-height:1.5}
.pager{text-align:right;margin-top:10px}
.pager i{display:inline-block;width:20px;height:14px;background:#ccc;margin-left:4px}

/* contact */
.contact{height:584px;background:var(--navy);color:#c5ccd5;padding-top:60px;position:relative}
.contact .section-title{color:var(--white)}
.contact-cols{display:flex;justify-content:space-between;margin-top:50px}
.contact h6{font-size:16px;font-weight:800;color:var(--white);text-transform:uppercase;margin-bottom:20px}
.form{width:300px}
.field{display:flex;align-items:center;height:32px;margin-bottom:10px;font-size:13px}
.field span{width:90px}
.field i{flex:1;height:30px;background:var(--white);display:block}
.field.tall{height:64px;align-items:flex-start}
.field.tall i{height:64px}
.form .btn{margin-left:90px;margin-top:6px;padding:8px 24px;font-size:13px}
.truck-art{width:300px;height:280px;background:radial-gradient(ellipse at center,rgba(255,255,255,.14),rgba(255,255,255,0) 70%)}
.details{width:300px;font-size:13px}
.detail{display:flex;gap:12px;margin-bottom:14px;line-height:1.45}
.detail .ic{width:30px;height:30px;border-radius:50%;background:var(--navy-2);flex:none;display:flex;align-items:center;justify-content:center}
.detail b{color:var(--white);display:block}
.follow{display:flex;gap:8px;margin-top:6px}
.follow i{width:28px;height:28px;background:var(--orange);display:block}
.copyright{position:absolute;left:0;right:0;bottom:14px;text-align:center;font-size:13px;color:#8a95a3}
</style>
</head>
<body>

<header class="hero">
  <div class="hero-photo" role="img" aria-label="Cargo plane, container ship and semi truck in a blue sky transport scene"></div>
  <nav class="nav">
    <a class="active">Home</a><a>About Us</a><a>Services</a>
    <span class="spacer"></span>
    <a>Products</a><a>News</a><a>Contact Us</a>
  </nav>
  <div class="brand"><span class="brand-dot"></span><span class="brand-name">Northmark<br>Haul Co.</span></div>
  <div class="hero-copy">
    <h1>Consider it done!</h1>
    <span class="btn">Request a transport quote</span>
  </div>
</header>

<section class="about">
  <div class="wrap">
    <h2 class="section-title">About <span>Us</span></h2>
    <p>Northmark Haul Co. has been in business for over 10 years in the Intermodal Container business. We currently store containers for Calvera Ocean Lines, C. Ocean Lines of the Company and other line carriers. We also buy and sell containers. Email dispatch@northmarkhaul.example for inquiry on container purchase/sale items.</p>
    <p>Call us for all your intermodal container movement needs out of the Riverton, KS or MO area. We have been in business for over 10 years handling all types of container movement including heavy hauls to anywhere within the 48 states.</p>
  </div>
</section>

<section class="services">
  <div class="wrap">
    <h2 class="section-title">Our <span>Services</span></h2>
    <p class="lead">Lorem Ipsum is simply dummy text of the printing and typesetting industry. Lorem Ipsum has been the industry's standard dummy text ever since the 1500s, when an unknown printer took a galley of type and scrambled it to make a type specimen book.</p>
    <svg class="arrow l" viewBox="0 0 30 60"><path d="M24 4 6 30l18 26" fill="none" stroke="#bbb" stroke-width="3"/></svg>
    <svg class="arrow r" viewBox="0 0 30 60"><path d="M6 4l18 26L6 56" fill="none" stroke="#bbb" stroke-width="3"/></svg>
    <div class="cards">
      <article class="card">
        <div class="photo" role="img" aria-label="Semi truck on a highway" style="background:linear-gradient(180deg,#a7bccf,#4e5a66)"></div>
        <h3>Fastest Delivery Network</h3>
        <p>Lorem ipsum dolor sit amet, eiusmod tempor incididunt ut labore et dolore magna aliqua.</p>
        <span class="btn">Read More</span>
      </article>
      <article class="card">
        <div class="photo" role="img" aria-label="Container port with stacked shipping containers" style="background:linear-gradient(180deg,#c7d5e0,#8a6f5a)"></div>
        <h3>Solution With Technique</h3>
        <p>Lorem ipsum dolor sit amet, eiusmod tempor incididunt ut labore et dolore magna aliqua.</p>
        <span class="btn">Read More</span>
      </article>
      <article class="card">
        <div class="photo" role="img" aria-label="Red truck hauling a container" style="background:linear-gradient(180deg,#b8cde0,#8c4a3f)"></div>
        <h3>Transload</h3>
        <p>Lorem ipsum dolor sit amet, eiusmod tempor incididunt ut labore et dolore magna aliqua.</p>
        <span class="btn">Read More</span>
      </article>
    </div>
  </div>
</section>

<section class="why">
  <div class="wrap">
    <h2 class="section-title">Why <span>Choose Us</span></h2>
    <div class="why-grid">
      <div class="person" role="img" aria-label="Smiling businessman in a suit holding a tablet"></div>
      <div class="feature left hot" style="left:20px;top:20px">
        <div class="icon"><svg width="22" height="22" viewBox="0 0 24 24"><path d="M2 10h4v12H2zM8 22h10l4-9v-3h-7l1-6-2-2-6 8z" fill="#fff"/></svg></div>
        <h4>100% Satisfied Customers</h4>
        <p>Lorem ipsum dolor sit amet, eiusmod tempor incididunt ut labore.</p>
      </div>
      <div class="feature left" style="left:20px;top:250px">
        <div class="icon"><svg width="24" height="24" viewBox="0 0 24 24"><path d="M1 6h13v10H1zM14 9h5l4 4v3h-9z" fill="#fff"/><circle cx="5" cy="18" r="2" fill="#fff"/><circle cx="18" cy="18" r="2" fill="#fff"/></svg></div>
        <h4>Modern Vehicles Fleet</h4>
        <p>Lorem ipsum dolor sit amet, eiusmod tempor incididunt ut labore.</p>
      </div>
      <div class="feature" style="left:740px;top:70px">
        <div class="icon"><svg width="22" height="22" viewBox="0 0 24 24"><path d="M3 7l9-4 9 4v10l-9 4-9-4z" fill="none" stroke="#fff" stroke-width="2"/></svg></div>
        <h4>Fully Safe Delivers</h4>
        <p>Lorem ipsum dolor sit amet, eiusmod tempor incididunt ut labore.</p>
      </div>
      <div class="feature" style="left:740px;top:250px">
        <div class="icon"><svg width="22" height="22" viewBox="0 0 24 24"><path d="M6 2l4 5-2 2c1 3 4 6 7 7l2-2 5 4-3 4C10 21 3 14 2 5z" fill="#fff"/></svg></div>
        <h4>24/7 Support</h4>
        <p>Lorem ipsum dolor sit amet, eiusmod tempor incididunt ut labore.</p>
      </div>
    </div>
  </div>
</section>

<section class="team">
  <div class="wrap">
    <h2 class="section-title">Our <span>Team</span></h2>
    <div class="members">
      <div class="member" role="img" aria-label="Portrait of team member Alma Verhoek"><div class="cap"><b>Alma Verhoek</b><small>Owner</small></div></div>
      <div class="member open"><b>Tobias Verhoek</b><small>Manager</small><p>Lorem ipsum dolor sit amet, consectetur adipiscing elit, sed do eiusmod tempor incididunt ut labore et dolore.</p><div class="socials"><i></i><i></i><i></i><i></i></div></div>
      <div class="member" role="img" aria-label="Portrait of team member Jana Ostrell"><div class="cap"><b>Jana Ostrell</b><small>Head Supervisor</small></div></div>
      <div class="member" role="img" aria-label="Portrait of team member Bria Verhoek"><div class="cap"><b>Bria Verhoek</b><small>General Manager</small></div></div>
    </div>
  </div>
</section>

<section class="wrap split">
  <div class="news">
    <h2 class="section-title left">Latest <span>News</span></h2>
    <div class="news-item">
      <div class="thumb" role="img" aria-label="Red truck on the road"></div>
      <div><h5>Lorem ipsum dolor consectetur adipiscing elit sed.</h5><p>Sed diam nonummy nibh euismod tincidunt ut laoreet dolore magna aliquam erat volutpat.</p><time>January 4, 2016</time></div>
    </div>
    <div class="news-item">
      <div class="thumb" role="img" aria-label="Truck fleet at a depot"></div>
      <div><h5>Lorem ipsum dolor consectetur adipiscing elit sed.</h5><p>Sed diam nonummy nibh euismod tincidunt ut laoreet dolore magna aliquam erat volutpat.</p><time>January 4, 2016</time></div>
    </div>
    <span class="btn">View All News</span>
  </div>
  <div class="testis">
    <h2 class="section-title left">Client <span>Testimonials</span></h2>
    <div class="testi-box">
      <div class="testi"><div class="avatar" role="img" aria-label="Client portrait"></div><div><b>Mr. Leon Harcott</b><p>Lorem ipsum dolor sit amet, consectetuer adipiscing elit, sed diam nonummy nibh euismod tincidunt ut laoreet dolore magna aliquam erat volutpat.</p></div></div>
      <div class="testi"><div class="avatar" role="img" aria-label="Client portrait"></div><div><b>Mrs. Nell Harcott</b><p>Lorem ipsum dolor sit amet, consectetuer adipiscing elit, sed diam nonummy nibh euismod tincidunt ut laoreet dolore magna aliquam erat volutpat.</p></div></div>
      <div class="pager"><i></i><i></i></div>
    </div>
  </div>
</section>

<footer class="contact">
  <div class="wrap">
    <h2 class="section-title">Get in Touch</h2>
    <div class="contact-cols">
      <div class="form">
        <h6>Quick Inquiry</h6>
        <div class="field"><span>Name</span><i></i></div>
        <div class="field"><span>Email</span><i></i></div>
        <div class="field"><span>Phone</span><i></i></div>
        <div class="field tall"><span>Message</span><i></i></div>
        <span class="btn">Submit</span>
      </div>
      <div class="truck-art" role="img" aria-label="Faint semi truck illustration"></div>
      <div class="details">
        <h6>Contact Details</h6>
        <div class="detail"><span class="ic"><svg width="14" height="14" viewBox="0 0 24 24"><path d="M12 2a7 7 0 0 0-7 7c0 5 7 13 7 13s7-8 7-13a7 7 0 0 0-7-7z" fill="#f26522"/></svg></span><div><b>Northmark Haul Co.</b>Lorem ipsum dummy text of the printing industry.</div></div>
        <div class="detail"><span class="ic"><svg width="14" height="14" viewBox="0 0 24 24"><path d="M2 5h20v14H2z M2 5l10 8 10-8" fill="none" stroke="#f26522" stroke-width="2"/></svg></span><div><b>Email</b>dispatch@northmarkhaul.example</div></div>
        <div class="detail"><span class="ic"><svg width="14" height="14" viewBox="0 0 24 24"><path d="M6 2l4 5-2 2c1 3 4 6 7 7l2-2 5 4-3 4C10 21 3 14 2 5z" fill="#f26522"/></svg></span><div><b>Call Us</b>555-204-7810</div></div>
        <h6 style="margin:18px 0 6px">Follow Us</h6>
        <div class="follow"><i></i><i></i><i></i></div>
      </div>
    </div>
  </div>
  <p class="copyright">Copyright © 2016 Northmark Haul Co. | All Rights Reserved</p>
</footer>

</body>
</html>
```